Bref créative
Business Cards - Skyline Assessors
Two sided business cards
Simple
Corwin Hask
Certified Appraiser
48270 Millbrook Lane #1174
Sterling, VA 20391
corwin@plumvexa.com
www.plumvexa.com
Just the logo, either include the text or not (what ever looks better)
Colors and Fonts Guide

```html
<!DOCTYPE html>
<html lang="en">
<head>
<meta charset="utf-8">
<title>Skyline Assessors — Stationery</title>
<link href="https://fonts.googleapis.com/css2?family=Open+Sans:wght@400;600&display=swap" rel="stylesheet">
<style>
  :root {
    --brand-red: #b31f2a;
    --deep-red: #7d1119;
    --brand-blue: #1e5a8a;
    --deep-blue: #123a5c;
    --paper: #ffffff;
    --paper-edge: #d9dde2;
    --ink: #4a4f55;
    --soft-ink: #8a9098;
    --backdrop: #ffffff;
  }
  * { box-sizing: border-box; margin: 0; padding: 0; }
  html, body { width: 1200px; height: 302px; overflow: hidden; background: var(--backdrop); }
  .canvas { position: relative; width: 1200px; height: 302px; font-family: "Open Sans", sans-serif; color: var(--ink); }
  .brand-name { font-family: "Open Sans", sans-serif; font-weight: 600; color: var(--brand-red); line-height: 1.2; white-space: nowrap; }
  .piece { position: absolute; background: var(--paper); border: 1px solid var(--paper-edge); box-shadow: 0 2px 4px rgba(0,0,0,.18); overflow: hidden; }
  .tiny { font-size: 4.5px; line-height: 1.35; color: var(--soft-ink); }

  /* master wordmark */
  .hero-logo { position: absolute; left: 16px; top: 30px; width: 220px; text-align: center; }
  .hero-logo .brand-name { font-size: 20px; }
  .hero-logo .tagline { font-size: 7px; color: var(--soft-ink); margin-top: 8px; letter-spacing: .5px; }

  /* business cards */
  .card { width: 132px; height: 80px; }
  .card .brand-name { position: absolute; left: 0; right: 0; top: 28px; text-align: center; font-size: 10px; }
  .card .band { position: absolute; left: 0; right: 0; bottom: 0; height: 10px; background: linear-gradient(90deg, var(--brand-red), var(--deep-red)); }
  .card .band::after { content: ""; position: absolute; right: 0; top: -3px; width: 60%; height: 3px; background: var(--brand-blue); }
  .card-back .brand-name { top: 10px; left: 8px; right: auto; text-align: left; font-size: 8px; }
  .card-back .holder { position: absolute; left: 8px; top: 40px; }
  .card-back .holder strong { display: block; font-size: 6px; color: var(--ink); font-weight: 600; }
  .card-red { background: linear-gradient(135deg, var(--brand-red), var(--deep-red)); }
  .card-red .brand-name { color: var(--paper); }

  /* letterheads */
  .letterhead { top: 12px; width: 184px; height: 286px; }
  .letterhead .brand-name { position: absolute; left: 0; right: 0; top: 26px; text-align: center; font-size: 9px; }
  .letterhead .sender { position: absolute; left: 12px; top: 10px; }
  .letterhead .footer { position: absolute; left: 0; right: 0; bottom: 0; height: 12px; background: var(--brand-blue); }
  .letterhead .footer::before { content: ""; position: absolute; left: 0; right: 0; top: -3px; height: 3px; background: var(--brand-red); }
  .letterhead .site { position: absolute; left: 0; right: 0; bottom: 18px; text-align: center; }

  /* compliment slips */
  .slip { left: 696px; width: 180px; height: 118px; }
  .slip .brand-name { position: absolute; left: 0; right: 0; top: 14px; text-align: center; font-size: 8px; }
  .slip .footer { position: absolute; left: 0; right: 0; bottom: 0; height: 8px; background: var(--brand-blue); }
  .slip .footer::before { content: ""; position: absolute; left: 0; right: 0; top: -2px; height: 2px; background: var(--brand-red); }
  .slip .site { position: absolute; right: 10px; bottom: 14px; }

  /* envelopes */
  .envelope { position: absolute; left: 892px; width: 296px; }
  .envelope svg { position: absolute; inset: 0; }
  .envelope .label { position: absolute; font-family: "Open Sans", sans-serif; font-weight: 600; font-size: 9px; white-space: nowrap; }
  .envelope .return { position: absolute; white-space: nowrap; }
</style>
</head>
<body>
<main class="canvas">

  <header class="hero-logo">
    <div class="brand-name">Skyline Assessors</div>
    <p class="tagline">Corwin Hask</p>
  </header>

  <section class="piece card card-front" style="left:12px; top:116px;">
    <div class="brand-name">Skyline Assessors</div>
    <div class="band"></div>
  </section>
  <section class="piece card card-back" style="left:156px; top:116px;">
    <div class="brand-name">Skyline Assessors</div>
    <div class="holder tiny">
      <strong>Corwin Hask</strong>
      Certified Appraiser<br>
      48270 Millbrook Lane #1174<br>
      Sterling, VA 20391<br>
      corwin@plumvexa.com · www.plumvexa.com
    </div>
    <div class="band"></div>
  </section>
  <section class="piece card card-front" style="left:12px; top:210px;">
    <div class="brand-name" style="top:33px;">Skyline Assessors</div>
  </section>
  <section class="piece card card-red" style="left:156px; top:210px;">
    <div class="brand-name" style="top:33px;">Skyline Assessors</div>
  </section>

  <article class="piece letterhead" style="left:296px;">
    <div class="sender tiny">48270 Millbrook Lane #1174<br>Sterling, VA 20391</div>
    <div class="brand-name">Skyline Assessors</div>
    <div class="site tiny">www.plumvexa.com</div>
    <div class="footer"></div>
  </article>
  <article class="piece letterhead" style="left:498px;">
    <div class="brand-name">Skyline Assessors</div>
    <div class="site tiny">corwin@plumvexa.com · www.plumvexa.com</div>
    <div class="footer"></div>
  </article>

  <article class="piece slip" style="top:24px;">
    <div class="brand-name">Skyline Assessors</div>
    <div class="site tiny">www.plumvexa.com</div>
    <div class="footer"></div>
  </article>
  <article class="piece slip" style="top:170px;">
    <div class="brand-name">Skyline Assessors</div>
    <div class="site tiny">www.plumvexa.com</div>
    <div class="footer"></div>
  </article>

  <div class="envelope" style="top:14px; height:110px;">
    <svg viewBox="0 0 296 110" width="296" height="110">
      <defs>
        <linearGradient id="env-blue" x1="0" y1="0" x2="0" y2="1">
          <stop offset="0" stop-color="#1e5a8a"/>
          <stop offset="1" stop-color="#123a5c"/>
        </linearGradient>
      </defs>
      <rect x="0" y="0" width="296" height="110" fill="url(#env-blue)"/>
      <path d="M0 0 L148 48 L296 0" fill="none" stroke="rgba(255,255,255,.25)" stroke-width="1"/>
    </svg>
    <span class="label" style="left:0; right:0; text-align:center; top:22px; color:var(--paper);">Skyline Assessors</span>
  </div>
  <div class="envelope" style="top:90px; height:96px;">
    <svg viewBox="0 0 296 96" width="296" height="96">
      <rect x="0" y="0" width="296" height="96" fill="#ffffff" stroke="#d9dde2"/>
      <path d="M0 0 L148 40 L296 0 Z" fill="#b31f2a"/>
    </svg>
    <span class="label" style="left:0; right:0; text-align:center; top:8px; color:var(--paper);">Skyline Assessors</span>
  </div>
  <div class="envelope" style="top:176px; height:120px;">
    <svg viewBox="0 0 296 120" width="296" height="120">
      <rect x="0" y="0" width="296" height="120" fill="#ffffff" stroke="#d9dde2"/>
      <path d="M0 0 L148 44 L296 0" fill="none" stroke="#d9dde2"/>
      <rect x="0" y="112" width="296" height="8" fill="#1e5a8a"/>
      <rect x="0" y="109" width="296" height="3" fill="#b31f2a"/>
    </svg>
    <span class="label" style="left:12px; top:56px; color:var(--brand-red);">Skyline Assessors</span>
    <span class="return tiny" style="left:12px; top:72px;">48270 Millbrook Lane #1174 · Sterling, VA 20391</span>
  </div>

</main>
</body>
</html>
```